Business Card Design Project

Need a business card for a web application development company based in Denver Colorado. Our tagline is "Building Your Business, Not Just a Web Site"

Double-sided design with logo, taglin on one side and contact details on other (+ any other design elements).

Can use either or both of our logos (both are attached to project in psd and eps format)

• Use blue and gray as the main color. Something similar to the color scheme of the home page of our web site (www.copperleaf-grid-makers.com)

```html
<!DOCTYPE html>
<html lang="en">
<head>
<meta charset="utf-8">
<title>Copperleaf Grid Makers – Business Card</title>
<link href="https://fonts.googleapis.com/css2?family=Open+Sans:wght@400;600;700&display=swap" rel="stylesheet">
<style>
  :root {
    --stage: #e6e6e6;
    --navy: #455072;
    --white: #ffffff;
    --brand-blue: #2f3f9c;
    --ink-navy: #1f2a6b;
    --label-grey: #8a8a8a;
    --label-blue: #3a4aa8;
    --caption: #111111;
  }
  * { margin: 0; padding: 0; box-sizing: border-box; }
  html, body { width: 1200px; height: 1020px; overflow: hidden; background: var(--stage); }
  body { font-family: "Open Sans", Arial, sans-serif; position: relative; }

  .side-caption {
    position: absolute;
    left: 915px;
    font-size: 84px;
    font-weight: 400;
    color: var(--caption);
    line-height: 1;
  }
  .side-caption--front { top: 150px; }
  .side-caption--back { top: 770px; }

  /* Front */
  .card-front {
    position: absolute;
    left: 12px; top: 12px;
    width: 649px; height: 486px;
    background: var(--navy);
    overflow: hidden;
  }
  .front-band {
    position: absolute;
    left: 0; top: 37px;
    width: 649px; height: 249px;
    background: var(--white);
    border-radius: 0 26px 26px 0;
  }
  .front-band-inner {
    position: absolute;
    left: 0; top: 18px;
    width: 629px; height: 213px;
    background: var(--navy);
    border-radius: 0 20px 20px 0;
  }
  .front-brand {
    position: absolute;
    left: 22px; top: 88px;
    display: flex; align-items: center; gap: 40px;
  }
  .front-brand-dot {
    width: 118px; height: 118px;
    border-radius: 50%;
    background: var(--white);
    flex: none;
  }
  .front-brand-name {
    color: var(--white);
    font-weight: 700;
    line-height: 1.05;
  }
  .front-brand-name .name-main { display: block; font-size: 54px; letter-spacing: 1px; }
  .front-brand-name .name-sub { display: block; font-size: 31px; letter-spacing: 3px; }
  .front-tagline {
    position: absolute;
    left: 202px; top: 222px;
    color: var(--white);
    font-size: 17px;
    font-weight: 400;
    font-style: normal;
    letter-spacing: 0.3px;
  }

  /* Back */
  .card-back {
    position: absolute;
    left: 12px; top: 512px;
    width: 859px; height: 488px;
    background: var(--white);
    overflow: hidden;
  }
  .back-brand {
    position: absolute;
    left: 24px; top: 16px;
    display: flex; align-items: center; gap: 30px;
  }
  .back-brand-dot {
    width: 84px; height: 84px;
    border-radius: 50%;
    background: var(--brand-blue);
    flex: none;
  }
  .back-brand-name {
    color: var(--brand-blue);
    font-weight: 700;
    line-height: 1.05;
  }
  .back-brand-name .name-main { display: block; font-size: 40px; letter-spacing: 0.5px; }
  .back-brand-name .name-sub { display: block; font-size: 23px; letter-spacing: 2.5px; }

  .holder {
    position: absolute;
    left: 2px; top: 344px;
    font-size: 19px;
    line-height: 30px;
    color: var(--label-grey);
  }
  .holder-label { color: var(--label-blue); }

  .contact-rule {
    position: absolute;
    left: 422px; top: 340px;
    width: 3px; height: 148px;
    background: var(--brand-blue);
  }
  .contact-list {
    position: absolute;
    left: 434px; top: 342px;
    list-style: none;
  }
  .contact-item {
    display: flex; align-items: center; gap: 12px;
    color: var(--ink-navy);
  }
  .contact-icon { width: 30px; flex: none; display: flex; justify-content: center; }
  .contact-item--phone { font-size: 26px; color: var(--brand-blue); height: 40px; }
  .contact-item--email { font-size: 21px; height: 40px; }
  .contact-item--email .contact-icon { font-size: 27px; line-height: 1; color: var(--caption); }
  .contact-item--address { font-size: 17px; line-height: 22px; align-items: flex-start; padding-top: 6px; }
</style>
</head>
<body>

  <section class="card-front" aria-label="Business card front">
    <div class="front-band"><div class="front-band-inner"></div></div>
    <div class="front-brand">
      <span class="front-brand-dot" aria-hidden="true"></span>
      <span class="front-brand-name">
        <span class="name-main">COPPERLEAF</span>
        <span class="name-sub">GRID MAKERS</span>
      </span>
    </div>
    <p class="front-tagline">Building Your Business, Not Just a Web Site</p>
  </section>
  <p class="side-caption side-caption--front">Front</p>

  <section class="card-back" aria-label="Business card back">
    <div class="back-brand">
      <span class="back-brand-dot" aria-hidden="true"></span>
      <span class="back-brand-name">
        <span class="name-main">COPPERLEAF</span>
        <span class="name-sub">GRID MAKERS</span>
      </span>
    </div>

    <div class="holder">
      <p><span class="holder-label">Name</span> : Abc</p>
      <p><span class="holder-label">Desigantion</span> : Xyz</p>
    </div>

    <div class="contact-rule"></div>
    <ul class="contact-list">
      <li class="contact-item contact-item--phone">
        <span class="contact-icon">
          <svg width="26" height="22" viewBox="0 0 28 24" aria-hidden="true">
            <path d="M2 8c0-4 5-6 12-6s12 2 12 6v2h-6V7H8v3H2z" fill="#111"/>
            <path d="M7 11h14l4 11H3z" fill="#111"/>
            <circle cx="14" cy="16" r="3" fill="#fff"/>
          </svg>
        </span>
        <span>303.555.0142</span>
      </li>
      <li class="contact-item contact-item--email">
        <span class="contact-icon">@</span>
        <span>dana@copperleaf-grid-makers.com</span>
      </li>
      <li class="contact-item contact-item--address">
        <span class="contact-icon">
          <svg width="26" height="24" viewBox="0 0 28 26" aria-hidden="true">
            <path d="M14 1L1 13h4v12h7v-8h4v8h7V13h4z" fill="#111"/>
          </svg>
        </span>
        <span>2400 Larkspur Court Suite 210<br>Broomfield, CO 80020</span>
      </li>
    </ul>
  </section>
  <p class="side-caption side-caption--back">Back</p>

</body>
</html>
```